Civora - a Political Plebescite app.

There is a current app in the App Store (worldwide) and Play Store (worldwide) called yourTally (with an owl logo). The UX needs to be redesigned to make it more visually pleasing.

The requirement is to build a UX that is suitable for both iOS and Android - i.e. consistent look for both platforms. The design is to span the variety of sizes available from smart devices - phones and tablets. The layout as it stands is portrait only, and a secondary design to encompass landscape is wanted.

You would need to download the app to get a feel for all the functionality - there are 3 visible forms (currently) and a hidden form, that will be used in the near future - this hidden form will look similar to the main (first) form.

To get full functionality you need to do the following:
Go to the Options page
Toggle the top slide
Click on UNREGISTERED
Select a state/territory

I know this is a bit non-intuitive - in the "real" product these steps are automated - but for this release the user gets to choose.

Once this is done - the other button(s) appear in the top left of the screen - and data is available to be displayed.

The current forms are included in this brief. The Options screen will ultimately not be showing all the current data, only the lower slider (or other indicator) and the associated version and copyright notices. The hidden screen is much like the main screen - showing the name of the bill and information pertaining to that bill - there needs to be a button (or action site) to toggle between the main and this hidden screen.

Target Market(s)

All eligable voters (currently in Australia)

Industry/Entity Type

Political

Requirements
Should not have
• Do not present to me my own/existing design with the only change being colours and label layout.

```html
<!DOCTYPE html>
<html lang="en">
<head>
<meta charset="utf-8">
<title>Civora – Bill Vote</title>
<link rel="stylesheet" href="https://fonts.googleapis.com/css2?family=Inter:wght@300;400;500;700&display=swap">
<style>
:root{
  --bar-bg:#ebebeb;
  --bar-line:#c8c8c8;
  --ink:#1a1a1a;
  --link:#1a8cff;
  --card-blue:#0a7cff;
  --card-foot:#bdbdbd;
  --side-body:#ebebeb;
  --screen:#ffffff;
  --online:#2ecc71;
  --yes:#2ecc71;
  --abstain:#f4d568;
  --no:#ec6a4f;
  --icon:#222222;
}
*{box-sizing:border-box;margin:0;padding:0}
html,body{width:676px;height:1200px;overflow:hidden;background:var(--screen)}
body{font-family:"Inter","Helvetica Neue",Arial,sans-serif;color:var(--ink);position:relative}

.status-bar{position:absolute;top:0;left:0;width:676px;height:46px;background:var(--bar-bg);font-size:20px;font-weight:500}
.status-bar .signal{position:absolute;left:14px;top:13px;display:flex;gap:3px;align-items:center}
.status-bar .signal span{width:9px;height:9px;border-radius:50%;background:var(--ink)}
.status-bar .wifi{margin-left:4px}
.status-bar .time{position:absolute;left:0;right:0;top:11px;text-align:center}
.status-bar .battery{position:absolute;right:12px;top:11px;display:flex;align-items:center;gap:4px;font-weight:400}
.battery-shell{width:42px;height:19px;border:2px solid var(--ink);border-radius:4px;padding:2px;position:relative}
.battery-shell::after{content:"";position:absolute;right:-5px;top:5px;width:3px;height:6px;background:var(--ink);border-radius:0 2px 2px 0}
.battery-shell i{display:block;width:100%;height:100%;background:var(--ink);border-radius:1px}

.nav-bar{position:absolute;top:46px;left:0;width:676px;height:92px;background:var(--bar-bg);border-bottom:1px solid var(--bar-line)}
.nav-link{position:absolute;top:43px;font-size:23px;color:var(--link);font-weight:400}
.nav-link.help{left:25px}
.nav-link.settings{right:20px}
.assembly{position:absolute;left:0;right:0;top:22px;text-align:center}
.assembly .label{font-size:13px;font-weight:700;letter-spacing:.3px}
.assembly .region{font-size:28px;font-weight:300;margin-top:4px;display:inline-flex;align-items:center;gap:12px}
.assembly .region svg{width:14px;height:9px}

.screen-edge{position:absolute;top:138px;right:1px;width:1px;height:1062px;background:var(--bar-line)}

.progress{position:absolute;top:160px;left:0;right:0;text-align:center;font-size:25px;font-weight:700}
.status-pill{position:absolute;left:514px;top:159px;width:141px;height:34px;border:1px solid #9a9a9a;border-radius:17px;display:flex;align-items:center;justify-content:center;gap:9px;font-size:19px;font-weight:700}
.status-pill .dot{width:14px;height:14px;border-radius:50%;background:var(--online)}

.bill-card{position:absolute;top:215px;width:437px;height:772px;border-radius:12px;overflow:hidden;background:#fff;box-shadow:0 1px 4px rgba(0,0,0,.25)}
.bill-card.prev{left:-345px}
.bill-card.next{left:585px}
.bill-card.current{left:120px}
.bill-head{background:var(--card-blue);color:#fff;height:140px;padding:22px 24px 0}
.bill-title{font-size:23px;font-weight:700;line-height:1.1;white-space:nowrap}
.bill-sub{font-size:15.5px;font-weight:300;line-height:1.3;white-space:nowrap}
.bill-year{font-size:16px;font-weight:700;margin-top:14px}
.bill-body{padding:28px 24px 0;font-size:23.4px;font-weight:300;line-height:31px;height:555px;white-space:nowrap}
.bill-card.prev .bill-body{background:var(--side-body)}
.bill-foot{position:absolute;left:0;bottom:0;width:100%;height:77px;background:var(--card-foot);display:flex;align-items:center;justify-content:center;font-size:23px;font-weight:700;letter-spacing:.5px}

.vote-btn{position:absolute;border-radius:50%;background:#fff;box-shadow:0 1px 4px rgba(0,0,0,.25);display:flex;align-items:center;justify-content:center}
.vote-btn .face{border-radius:50%;display:flex;align-items:center;justify-content:center}
.vote-btn.yes{left:120px;top:1025px;width:142px;height:142px}
.vote-btn.no{left:415px;top:1025px;width:142px;height:142px}
.vote-btn.yes .face,.vote-btn.no .face{width:120px;height:120px}
.vote-btn.yes .face{background:var(--yes)}
.vote-btn.no .face{background:var(--no)}
.vote-btn.abstain{left:286px;top:1046px;width:100px;height:100px}
.vote-btn.abstain .face{width:80px;height:80px;background:var(--abstain)}
.vote-btn svg{width:50px;height:50px}
.abstain-bar{width:42px;height:13px;border-radius:7px;background:var(--icon)}
</style>
</head>
<body>
<header class="status-bar">
  <div class="signal"><span></span><span></span><span></span><span></span><span></span>
    <svg class="wifi" width="20" height="15" viewBox="0 0 20 15"><path d="M10 14 L6.5 10.2 A5 5 0 0 1 13.5 10.2 Z M2.5 6.3 A10.5 10.5 0 0 1 17.5 6.3 L15.6 8.2 A8 8 0 0 0 4.4 8.2 Z M-0.5 3.2 A15 15 0 0 1 20.5 3.2 L18.6 5.1 A12.5 12.5 0 0 0 1.4 5.1 Z" fill="#1a1a1a"/></svg>
  </div>
  <div class="time">9:41 AM</div>
  <div class="battery">100%<span class="battery-shell"><i></i></span></div>
</header>

<nav class="nav-bar">
  <span class="nav-link help">Help</span>
  <div class="assembly">
    <div class="label">LEGISLATIVE ASSEMBLY</div>
    <div class="region"><svg viewBox="0 0 14 9"><path d="M0 0h14L7 9z" fill="#1a1a1a"/></svg>Coral Territory</div>
  </div>
  <span class="nav-link settings">Settings</span>
</nav>
<div class="screen-edge"></div>

<div class="progress">4/10</div>
<div class="status-pill"><span class="dot"></span>ONLINE</div>

<article class="bill-card prev">
  <div class="bill-head">
    <div class="bill-title">Inspection of Places of Custody</div>
    <div class="bill-sub">(Independent Protocol for the Inspection of Custody)<br>&nbsp;- Shared Model Legislation</div>
    <div class="bill-year">Bill 2013</div>
  </div>
  <div class="bill-body">An act to enable the Custody Insp-<br>ection Scheme and the rules for<br>Humane and Safe Treatment of all<br>Persons held in Secure Facilities<br>to be given full effect within the<br>Territory.</div>
  <div class="bill-foot">VIEW BILL</div>
</article>

<article class="bill-card current">
  <div class="bill-head">
    <div class="bill-title">Inspection of Places of Custody</div>
    <div class="bill-sub">(Independent Protocol for the Inspection of Custody)<br>&nbsp;- Shared Model Legislation</div>
    <div class="bill-year">Bill 2013</div>
  </div>
  <div class="bill-body">An act to enable the Custody Insp-<br>ection Scheme and the rules for<br>Humane and Safe Treatment of all<br>Persons held in Secure Facilities<br>to be given full effect within the<br>Territory.</div>
  <div class="bill-foot">VIEW BILL</div>
</article>

<article class="bill-card next">
  <div class="bill-head">
    <div class="bill-title">Inspection of Places of Custody</div>
    <div class="bill-sub">(Independent Protocol for the Inspection of Custody)<br>&nbsp;- Shared Model Legislation</div>
    <div class="bill-year">Bill 2013</div>
  </div>
  <div class="bill-body">An act to enable the Custody Insp-<br>ection Scheme and the rules for<br>Humane and Safe Treatment of all<br>Persons held in Secure Facilities<br>to be given full effect within the<br>Territory.</div>
  <div class="bill-foot">VIEW BILL</div>
</article>

<div class="vote-btn yes" aria-label="Vote yes"><div class="face">
  <svg viewBox="0 0 50 50"><rect x="37" y="20" width="9" height="24" rx="1.5" fill="#222"/><path d="M5 22 L16 14 L22 5 Q27 4 27 10 L26 18 L32 18 Q35 18 35 22 L35 41 Q35 44 32 44 L8 44 Q5 44 5 41 Z" fill="#222"/></svg>
</div></div>
<div class="vote-btn abstain" aria-label="Abstain"><div class="face"><span class="abstain-bar"></span></div></div>
<div class="vote-btn no" aria-label="Vote no"><div class="face">
  <svg viewBox="0 0 50 50"><g transform="rotate(180 25 25)"><rect x="37" y="20" width="9" height="24" rx="1.5" fill="#222"/><path d="M5 22 L16 14 L22 5 Q27 4 27 10 L26 18 L32 18 Q35 18 35 22 L35 41 Q35 44 32 44 L8 44 Q5 44 5 41 Z" fill="#222"/></g></svg>
</div></div>
</body>
</html>
```